Security Consulting firm needs an ad design

We need a 3.375” x 4.875” ad design for our core services. The ad should include the company logo and the content from the first half of the attached sample JPG (Without the sentence under the title but including the description for the Plan - Design - Deploy - Manage and the titles ) as well as the following corporate information:
www.corvanthpartners.us
82 Marbury Ave. Suite 615, Woodcliff Lake, NJ 07677
PHONE 888-416-2057 / EMAIL info@corvanthpartners.us
The design should incorporate the same blue color that is in our logo and the font Raleway. Also - please use the same icons that are in the sample JPG - they can also be extracted from the attached indesign file.
The ad is to be publish in print and digital issue.
Please provide with all source files as well as a hi-res PDF using press quality or similar PDF settings.
- Raleway

```html
<!DOCTYPE html>
<html lang="en">
<head>
<meta charset="UTF-8">
<title>Corvanth Partners – Creating Secure Environments</title>
<link href="https://fonts.googleapis.com/css2?family=Raleway:wght@300;400;500;700;800;900&display=swap" rel="stylesheet">
<style>
  :root{
    --page:#f1f2f4;
    --navy:#1b2135;
    --sky:#4d9fdc;
    --brand:#1f6ab4;
    --icon:#2a6fbf;
    --band:#e8f0f9;
    --footer:#0069ad;
    --ink:#1d1d1f;
    --white:#ffffff;
    --rule:#b9c4d0;
  }
  *{margin:0;padding:0;box-sizing:border-box}
  html,body{width:1200px;height:1200px;overflow:hidden;background:var(--page)}
  body{font-family:'Raleway',sans-serif;position:relative}

  .ad{position:absolute;left:226px;top:60px;width:748px;height:1080px;background:var(--band);overflow:hidden;box-shadow:0 6px 24px rgba(0,0,0,.18)}

  .hero{position:absolute;left:0;top:0;width:748px;height:581px;
    background:
      linear-gradient(100deg,var(--navy) 0%,var(--navy) 30%,rgba(27,33,53,.55) 52%,rgba(27,33,53,0) 75%),
      linear-gradient(160deg,#8c9a8f 0%,#6f7d84 30%,#4f5f6c 55%,#3d5560 75%,#5d7a5c 100%);}

  .brand{position:absolute;left:60px;top:104px;display:flex;align-items:center;gap:14px}
  .brand-dot{width:44px;height:44px;border-radius:50%;background:var(--sky)}
  .brand-name{font-weight:700;font-size:44px;color:var(--sky);letter-spacing:-.5px;line-height:1}

  .headline{position:absolute;left:52px;top:232px;line-height:1}
  .headline .lead{display:block;font-weight:300;font-size:66px;color:var(--white);letter-spacing:-1px}
  .headline .key{display:block;font-weight:900;font-size:130px;color:var(--sky);letter-spacing:-4px;margin-top:6px}
  .headline .tail{display:block;font-weight:800;font-size:64px;color:var(--sky);letter-spacing:-1px;margin-top:2px}

  .service-badge{position:absolute;top:527px;width:108px;height:108px;margin-left:-54px;border-radius:50%;background:var(--white);
    box-shadow:0 4px 8px rgba(0,0,0,.28);display:flex;align-items:center;justify-content:center}
  .service-badge svg{width:54px;height:54px}

  .service{position:absolute;top:680px;width:170px;margin-left:-85px;text-align:center}
  .service h3{font-weight:700;font-size:23px;color:var(--brand);margin-bottom:8px}
  .service p{font-weight:400;font-size:19px;line-height:1.13;color:var(--ink)}

  .divider{position:absolute;top:663px;height:165px;width:1.5px;background:var(--rule)}

  .contact{position:absolute;left:0;top:857px;width:748px;height:223px;background:var(--footer);color:var(--white)}
  .web{position:absolute;left:0;width:100%;top:44px;text-align:center;font-weight:700;font-size:33px}
  .reach{position:absolute;left:72px;top:106px}
  .phone{display:flex;align-items:center;gap:10px;font-weight:800;font-size:31px}
  .email{display:flex;align-items:center;gap:12px;font-weight:400;font-size:20px;margin-top:4px;padding-left:2px}
  .reach svg{flex:none}
  .contact-rule{position:absolute;left:378px;top:108px;width:1.5px;height:80px;background:rgba(255,255,255,.45)}
  .address{position:absolute;left:414px;top:112px;display:flex;gap:8px;font-size:22px;font-weight:400;line-height:1.25}
  .address svg{margin-top:4px;flex:none}
</style>
</head>
<body>
<div class="ad">
  <div class="hero" role="img" aria-label="Aerial photograph of a large crowd gathered along a road, fading into dark navy on the left"></div>

  <div class="brand">
    <span class="brand-dot"></span>
    <span class="brand-name">Corvanth Partners</span>
  </div>

  <h1 class="headline">
    <span class="lead">CREATING</span>
    <span class="key">SECURE</span>
    <span class="tail">ENVIRONMENTS</span>
  </h1>

  <div class="service-badge" style="left:110px">
    <svg viewBox="0 0 48 48" fill="none" stroke="var(--icon)" stroke-width="3" stroke-linecap="round" stroke-linejoin="round">
      <rect x="9" y="7" width="30" height="37" rx="3"/>
      <rect x="17" y="3" width="14" height="7" rx="2" fill="var(--icon)"/>
      <path d="M14 18l3 3 5-5M14 27l3 3 5-5M14 36l3 3 5-5M26 19h8M26 28h8M26 37h8"/>
    </svg>
  </div>
  <div class="service-badge" style="left:286px">
    <svg viewBox="0 0 48 48" fill="var(--icon)">
      <path d="M21 3h6l1 6 4 2 5-4 4 4-4 5 2 4 6 1v6l-6 1-2 4 4 5-4 4-5-4-4 2-1 6h-6l-1-6-4-2-5 4-4-4 4-5-2-4-6-1v-6l6-1 2-4-4-5 4-4 5 4 4-2z"/>
      <circle cx="24" cy="24" r="8" fill="#fff"/>
      <path d="M18 16l8 8-2 2-8-8a5 5 0 0 1 2-2zM26 24l14 14-3 3-14-14z" stroke="#fff" stroke-width="2"/>
    </svg>
  </div>
  <div class="service-badge" style="left:463px">
    <svg viewBox="0 0 48 48" fill="var(--icon)">
      <path d="M44 4c-10 0-18 5-24 14l10 10c9-6 14-14 14-24z"/>
      <circle cx="33" cy="15" r="3.5" fill="#fff"/>
      <path d="M19 19l-9 1-6 7 9 1zM29 29l-1 9-7 6-1-9z"/>
      <path d="M14 32c-4 1-7 5-8 10 5-1 9-4 10-8z"/>
    </svg>
  </div>
  <div class="service-badge" style="left:640px">
    <svg viewBox="0 0 48 48" fill="var(--icon)" stroke="var(--icon)" stroke-width="2.5">
      <circle cx="24" cy="10" r="6" stroke="none"/>
      <path d="M14 26c0-6 4-9 10-9s10 3 10 9z" stroke="none"/>
      <path d="M24 26v14M6 30l18-4 18 4" fill="none"/>
      <circle cx="6" cy="30" r="3.5" stroke="none"/>
      <circle cx="42" cy="30" r="3.5" stroke="none"/>
      <circle cx="24" cy="41" r="3.5" stroke="none"/>
    </svg>
  </div>

  <div class="service" style="left:110px"><h3>PLAN</h3><p>Security<br>assessment<br>and planning<br>services</p></div>
  <div class="divider" style="left:201px"></div>
  <div class="service" style="left:286px"><h3>DESIGN</h3><p>Security<br>design and<br>engineering</p></div>
  <div class="divider" style="left:377px"></div>
  <div class="service" style="left:463px"><h3>DEPLOY</h3><p>Procurement<br>and Project<br>Management<br>Services</p></div>
  <div class="divider" style="left:553px"></div>
  <div class="service" style="left:640px"><h3>MANAGE</h3><p>Comprehensive<br>security<br>program<br>management</p></div>

  <footer class="contact">
    <div class="web">www.corvanthpartners.us</div>
    <div class="reach">
      <div class="phone">
        <svg width="16" height="16" viewBox="0 0 24 24" fill="#fff"><path d="M6.6 10.8a15 15 0 0 0 6.6 6.6l2.2-2.2a1 1 0 0 1 1-.25 11.4 11.4 0 0 0 3.6.57 1 1 0 0 1 1 1V20a1 1 0 0 1-1 1A17 17 0 0 1 3 4a1 1 0 0 1 1-1h3.5a1 1 0 0 1 1 1c0 1.25.2 2.45.57 3.6a1 1 0 0 1-.25 1z"/></svg>
        <span>888-416-2057</span>
      </div>
      <div class="email">
        <svg width="15" height="11" viewBox="0 0 20 14" fill="#fff"><path d="M0 0h20v14H0z"/><path d="M0 0l10 8 10-8" fill="none" stroke="var(--footer)" stroke-width="1.6"/></svg>
        <span>info@corvanthpartners.us</span>
      </div>
    </div>
    <div class="contact-rule"></div>
    <div class="address">
      <svg width="13" height="18" viewBox="0 0 12 18" fill="none" stroke="#fff" stroke-width="2"><path d="M6 17S1 10 1 6a5 5 0 0 1 10 0c0 4-5 11-5 11z"/><circle cx="6" cy="6" r="1.8"/></svg>
      <span>82 Marbury Ave. Suite 615,<br>Alder Crossing, NJ 07390</span>
    </div>
  </footer>
</div>
</body>
</html>
```